Medical IT Business with New logo needs a fresh stationary design

First time on sketch Harbor; Thought I would give it a go.
This project is for business cards alone but we have loads of design work that needs to take place in the immediate future.

We provide IT services to the Medical Industry and value ourselves as offering a premium product to the market.

I am after a fresh, clean design using full colour 2 sided cards which includes our current colour palettes from our logo.

Card's must include:
- Logo
- Slogan
- Name
- Adress
- Email
- Phone
- Fax
- Mobile

Target Market(s)

Surgeons, High Profile Medical Personnel

Industry/Entity Type

Business

Fonts, CMYK Colours and Logo files attached.

Requirements
Must have
• Card's must include:
• - Logo
• - Slogan
• - Name
• - Adress
• - Email
• - Phone
• - Fax
• - Mobile
Nice to have
• Needs to incorporate our colour palette (attached CMYK colours)
Should not have
• Black backgrounds. Black text ok.

```html
<!DOCTYPE html>
<html lang="en">
<head>
<meta charset="utf-8">
<title>Clinora Systems – Business Cards</title>
<link href="https://fonts.googleapis.com/css2?family=Open+Sans:wght@400;600;700&display=swap" rel="stylesheet">
<style>
  :root {
    --navy: #1c3a72;
    --navy-deep: #1a3366;
    --brand-blue: #0a7fb8;
    --sky: #2f93d1;
    --lavender: #abb1cd;
    --white: #ffffff;
    --stage: #e8e5e0;
    --line-soft: rgba(255,255,255,0.75);
  }
  * { box-sizing: border-box; margin: 0; padding: 0; }
  html, body {
    width: 1200px; height: 864px; overflow: hidden;
    background: var(--stage);
    font-family: "Open Sans", Arial, sans-serif;
  }
  .canvas { position: relative; width: 1200px; height: 864px; }

  .card {
    position: absolute; width: 620px; height: 354px; overflow: hidden;
    box-shadow: 0 6px 18px rgba(0,0,0,0.18);
  }

  /* ---------- Back card ---------- */
  .card--back {
    left: 540px; top: 60px;
    background: linear-gradient(135deg, var(--navy-deep) 0%, var(--navy) 60%, #213f7a 100%);
  }
  .rule { position: absolute; height: 1px; background: var(--line-soft); }
  .rule--top { left: 250px; top: 112px; width: 350px; }
  .rule--bottom { left: 40px; top: 236px; width: 380px; }

  .brand { position: absolute; }
  .brand__name {
    font-weight: 700; font-size: 32px; line-height: 1; letter-spacing: 1px;
    text-transform: uppercase; white-space: nowrap;
  }
  .brand__slogan { font-size: 14px; margin-top: 8px; white-space: nowrap; }

  .card--back .brand { left: 250px; top: 142px; }
  .card--back .brand__name { color: var(--white); }
  .card--back .brand__slogan { color: var(--white); }

  .website {
    position: absolute; left: 0; right: 0; top: 282px; text-align: center;
    color: var(--sky); font-size: 20px; letter-spacing: 0.5px;
  }

  /* ---------- Front card ---------- */
  .card--front { left: 60px; top: 440px; background: var(--white); }
  .card-bands { position: absolute; inset: 0; width: 620px; height: 354px; }

  .card--front .brand { left: 40px; top: 44px; }
  .card--front .brand__name { color: var(--navy); }
  .card--front .brand__slogan { color: var(--brand-blue); }

  .contact {
    position: absolute; top: 200px; display: flex; flex-direction: column;
    align-items: center; gap: 4px; color: var(--white); font-size: 13px;
  }
  .contact svg { width: 28px; height: 28px; }
  .contact--phone { left: 28px; }
  .contact--mobile { left: 170px; }
  .contact--fax { left: 312px; }
  .contact--email { left: 450px; }

  .holder { position: absolute; left: 398px; top: 152px; display: flex; align-items: center; gap: 10px; }
  .holder svg { width: 32px; height: 32px; flex: none; }
  .holder__name { color: var(--white); font-size: 20px; line-height: 1.05; letter-spacing: 0.5px; }
  .holder__role { color: var(--brand-blue); font-size: 12px; font-weight: 600; }

  .address {
    position: absolute; left: 0; right: 0; top: 288px; text-align: center;
    color: var(--white); font-size: 15px; line-height: 1.35;
  }
</style>
</head>
<body>
<main class="canvas">

  <section class="card card--back" aria-label="Business card back">
    <div class="rule rule--top"></div>
    <div class="rule rule--bottom"></div>
    <div class="brand">
      <div class="brand__name">Clinora Systems</div>
      <div class="brand__slogan">IT care for every clinic</div>
    </div>
    <p class="website">www.website.com</p>
  </section>

  <section class="card card--front" aria-label="Business card front">
    <svg class="card-bands" viewBox="0 0 620 354" aria-hidden="true">
      <rect x="0" y="190" width="620" height="164" fill="var(--lavender)"/>
      <polygon points="350,190 386,146 620,146 620,190" fill="var(--lavender)"/>
      <line x1="380" y1="192" x2="620" y2="192" stroke="var(--white)" stroke-width="2"/>
      <polygon points="0,272 296,272 312,258 328,272 620,272 620,354 0,354" fill="var(--brand-blue)"/>
      <polyline points="0,269 296,269 312,255 328,269 620,269" fill="none" stroke="var(--white)" stroke-width="3"/>
    </svg>

    <div class="brand">
      <div class="brand__name">Clinora Systems</div>
      <div class="brand__slogan">IT care for every clinic</div>
    </div>

    <div class="holder">
      <svg viewBox="0 0 32 32" aria-hidden="true">
        <circle cx="16" cy="16" r="16" fill="var(--brand-blue)"/>
        <circle cx="16" cy="11" r="5" fill="var(--white)"/>
        <path d="M7 25c0-5 4-8 9-8s9 3 9 8z" fill="var(--white)"/>
      </svg>
      <div>
        <div class="holder__name">YOUR NAME</div>
        <div class="holder__role">Position</div>
      </div>
    </div>

    <div class="contact contact--phone">
      <svg viewBox="0 0 28 28" aria-hidden="true">
        <circle cx="14" cy="14" r="14" fill="var(--brand-blue)"/>
        <path d="M10 7l3 3-2 2c1 2 3 4 5 5l2-2 3 3-2 3c-5 0-11-6-11-11z" fill="var(--white)"/>
      </svg>
      <span>123.456.7890</span>
    </div>
    <div class="contact contact--mobile">
      <svg viewBox="0 0 28 28" aria-hidden="true">
        <rect x="9" y="3" width="11" height="22" rx="2" fill="var(--brand-blue)"/>
        <rect x="11" y="6" width="7" height="8" fill="var(--white)"/>
      </svg>
      <span>123.456.7890</span>
    </div>
    <div class="contact contact--fax">
      <svg viewBox="0 0 28 28" aria-hidden="true">
        <rect x="8" y="3" width="12" height="7" fill="var(--white)" stroke="var(--brand-blue)" stroke-width="2"/>
        <rect x="3" y="10" width="22" height="10" rx="2" fill="var(--brand-blue)"/>
        <rect x="8" y="17" width="12" height="8" fill="var(--white)" stroke="var(--brand-blue)" stroke-width="2"/>
      </svg>
      <span>123.456.7890</span>
    </div>
    <div class="contact contact--email">
      <svg viewBox="0 0 28 28" aria-hidden="true">
        <rect x="3" y="7" width="22" height="15" fill="var(--white)" stroke="var(--brand-blue)" stroke-width="2"/>
        <polyline points="3,7 14,16 25,7" fill="none" stroke="var(--brand-blue)" stroke-width="2"/>
      </svg>
      <span>youremail@clinora.com</span>
    </div>

    <p class="address">Address Here , Address Here,<br>Address Here</p>
  </section>

</main>
</body>
</html>
```